Career Counselor in need of a business card design

Hello Creatives! I'm in need of a business card design for a new company based in Georgia, USA called Pathways By Lumen.

Some things that may be helpful in creating your concept(s) include:

My Logo (Included in the Files section): There are three versions, two versions are in the second file. The all gold stacked (vertical) version is my primary logo and then there are two horizontal versions (one is all gold and the other is gold and grey).

My mission: to empower tweens through young adults to realize and actualize their CAREER ASPIRATIONS.
My vision: for tweens through young adults to LIVE LIFE ON PURPOSE and become CONTRIBUTING MEMBERS OF SOCIETY.

Biblical scriptures that support my ‘Why’: Psalms 127: 3-4(NIV) Children are a heritage from the Lord, offspring a reward from him. Like ARROWS in the hands of a warrior are children…. And Proverbs 29:18(JKV) Where there is no VISION, the people perish.

*Words in ALL CAPS are to emphasize what's important to me and may possibly provide you some inspiration (IDK - Have fun with it)!

Target Market(s)

My ideal customers are parents, guardians, and young adults.

Contact Information for Business Card

My name, degrees and credential: Delmira Fosket, M.S., Ed.S., NCC
Title: College and Career Coach and Consultant

Number: 555.317.8842
Address: 2618 Velbrook Avenue., Suite 407, Macon, GA 31299
Email: info@pathwaysbylumen.co
Website: www.pathwaysbylumen.co

My population: TWEENS • TEENS • EMERGING ADULTS
Services offered: One-On-One Sessions • Small Groups • Workshops

Colors

Designer to choose colors to be used in the design.

Requirements
Nice to have
• Either my mission or vision but I will understand if it does not all fit.
• My mission: To empower tweens through young adults to realize and actualize their career aspirations.
• My vision: For tweens through young adults to live life on purpose and become contributing members of society.

```html
<!DOCTYPE html>
<html lang="en">
<head>
<meta charset="utf-8">
<title>Pathways By Lumen — Business Card</title>
<link href="https://fonts.googleapis.com/css2?family=Cinzel:wght@400;500&family=Lato:wght@400&display=swap" rel="stylesheet">
<style>
  :root {
    --page-bg: #ecebe8;
    --gold-light: #f6d771;
    --gold-mid: #e2b84a;
    --gold-deep: #c99a2e;
    --gold-text: #d9ad3c;
    --ink: #2b2b2b;
    --grey-band: #8a8b8e;
    --white: #ffffff;
  }
  * { box-sizing: border-box; margin: 0; padding: 0; }
  html, body { width: 1200px; height: 900px; overflow: hidden; }
  body {
    background: var(--page-bg);
    position: relative;
    font-family: "Lato", Arial, sans-serif;
  }
  .card {
    position: absolute;
    left: 300px;
    width: 600px;
    height: 343px;
    overflow: hidden;
    box-shadow: 0 6px 18px rgba(0,0,0,0.18);
  }

  /* Back side */
  .card-back {
    top: 70px;
    background: linear-gradient(135deg, var(--gold-deep) 0%, var(--gold-light) 45%, var(--gold-mid) 100%);
    color: var(--white);
    text-align: center;
  }
  .vision {
    position: absolute;
    top: 78px;
    left: 0; right: 0;
    font-family: "Cinzel", Georgia, serif;
    font-size: 21px;
    line-height: 1.2;
    letter-spacing: 0.5px;
  }
  .back-rule {
    position: absolute;
    top: 262px;
    left: 60px; right: 60px;
    height: 1px;
    background: rgba(255,255,255,0.55);
  }
  .services {
    position: absolute;
    top: 280px;
    left: 0; right: 0;
    font-size: 14px;
    letter-spacing: 0.8px;
    text-transform: uppercase;
  }

  /* Front side */
  .card-front {
    top: 487px;
    background: var(--white);
  }
  .wave { position: absolute; inset: 0; width: 600px; height: 343px; }
  .holder-name {
    position: absolute;
    top: 26px; left: 36px;
    font-family: "Cinzel", Georgia, serif;
    font-weight: 400;
    font-size: 21px;
    color: var(--gold-text);
    letter-spacing: 0.5px;
  }
  .holder-title {
    position: absolute;
    top: 55px; left: 36px;
    font-size: 15px;
    color: var(--ink);
  }
  .brand {
    position: absolute;
    top: 80px; left: 326px;
    display: flex;
    align-items: center;
    gap: 14px;
  }
  .brand-dot {
    width: 60px; height: 60px;
    border-radius: 50%;
    background: var(--gold-text);
  }
  .brand-name {
    font-family: "Cinzel", Georgia, serif;
    font-size: 25px;
    line-height: 1.05;
    color: var(--gold-text);
    padding-left: 14px;
    border-left: 1px solid var(--gold-text);
  }
  .contact {
    position: absolute;
    top: 130px; left: 36px;
    list-style: none;
    font-size: 16px;
    color: var(--ink);
    line-height: 1.35;
  }
  .contact li { display: flex; align-items: center; gap: 8px; }
  .contact svg { width: 13px; height: 13px; fill: var(--gold-text); flex: none; }
  .contact .address { display: block; margin-top: 3px; font-size: 17px; line-height: 1.25; }
  .population {
    position: absolute;
    top: 250px; right: 22px;
    font-size: 14px;
    letter-spacing: 0.6px;
    color: var(--white);
    text-transform: uppercase;
  }
</style>
</head>
<body>

<section class="card card-back" aria-label="Card back">
  <p class="vision">For tweens through<br>young adults to live life<br>on purpose and become<br>contributing members of society.</p>
  <div class="back-rule"></div>
  <p class="services">One-on-One Sessions • Small Groups • Workshops</p>
</section>

<section class="card card-front" aria-label="Card front">
  <svg class="wave" viewBox="0 0 600 343" aria-hidden="true">
    <defs>
      <linearGradient id="goldSweep" x1="0" y1="1" x2="1" y2="0">
        <stop offset="0" stop-color="#c99a2e"/>
        <stop offset="0.5" stop-color="#f3d06a"/>
        <stop offset="1" stop-color="#d8ab3e"/>
      </linearGradient>
    </defs>
    <path d="M0,282 C200,292 390,195 600,140 L600,343 L0,343 Z" fill="var(--grey-band)"/>
    <path d="M0,306 C200,314 380,200 600,140 L600,343 L0,343 Z" fill="var(--white)"/>
    <path d="M0,314 C200,320 380,200 600,140 L600,343 L0,343 Z" fill="url(#goldSweep)"/>
  </svg>

  <h1 class="holder-name">DELMIRA FOSKET, M.S., ED.S., NCC</h1>
  <p class="holder-title">College and Career Coach and Consultant</p>

  <div class="brand">
    <span class="brand-dot"></span>
    <span class="brand-name">PATHWAYS<br>BY LUMEN</span>
  </div>

  <ul class="contact">
    <li><svg viewBox="0 0 16 16"><path d="M3 1h3l1.5 4-2 1.2a9 9 0 0 0 4.3 4.3L11 8.5l4 1.5v3a2 2 0 0 1-2 2A12 12 0 0 1 1 3a2 2 0 0 1 2-2z"/></svg>555.317.8842</li>
    <li><svg viewBox="0 0 16 16"><path d="M1 3h14v10H1z M1 3l7 6 7-6"/></svg>info@pathwaysbylumen.co</li>
    <li><svg viewBox="0 0 16 16"><circle cx="8" cy="8" r="7"/></svg>www.pathwaysbylumen.co</li>
    <li class="address">2618 Velbrook Avenue<br>Suite 407, Macon, GA 31299</li>
  </ul>

  <p class="population">Tweens • Teens • Emerging Adults</p>
</section>

</body>
</html>
```